Business card to be used as a flyer

This business card should do the trick of a full scale flyer , so basicaly from the business card itself we only keep the size and remove the clasical name , position , company name (etc).
This business cards should be , like said above, used as promo tool, being gived to different girls . So base one : the design is girls oriented.
Colors : black background . We will use gold (color) folio for the text.
Attached you have our logo, but this should not be a proiminent part of the design . You can use only the cat head instead.
Target Market(s)
Girls / Women
Contact Information for Business Card
> black background , gold / folio text and elements
> cat head from the logo in a creative way do be displayed
> proieminent text "your path to success starts here"
> contact details phone and website .
www.velmastrand.ro (website) and 0742163958 (phone)

```html
<!DOCTYPE html>
<html lang="en">
<head>
<meta charset="utf-8">
<title>Velma Strand Studio – Business Card</title>
<link rel="stylesheet" href="https://fonts.googleapis.com/css2?family=Bebas+Neue&family=Arimo:wght@400;700&display=swap">
<style>
  :root {
    --backdrop: #0e0e0f;
    --card: #232325;
    --card-edge: #d49a16;
    --gold: #e3a322;
    --gold-light: #f2c14a;
    --emboss-dark: #1c1c1e;
    --emboss-light: #2c2c2f;
  }
  * { margin: 0; padding: 0; box-sizing: border-box; }
  html, body {
    width: 1200px;
    height: 820px;
    overflow: hidden;
    background: var(--backdrop);
  }
  .stage {
    width: 1200px;
    height: 820px;
    display: flex;
    align-items: center;
    justify-content: center;
    gap: 40px;
  }
  .card {
    position: relative;
    width: 540px;
    height: 300px;
    background: var(--card);
    border: 1.5px solid var(--card-edge);
    overflow: hidden;
  }

  /* Back side: promo message */
  .promo-artwork {
    position: absolute;
    left: 250px;
    top: 24px;
    width: 270px;
    height: 276px;
    border-radius: 48% 52% 0 0 / 40% 40% 0 0;
    background: radial-gradient(ellipse at 45% 45%, var(--emboss-light) 0%, var(--emboss-dark) 70%, var(--card) 100%);
  }
  .promo-tagline {
    position: absolute;
    left: 36px;
    top: 60px;
    font-family: "Bebas Neue", sans-serif;
    font-size: 46px;
    line-height: 0.98;
    letter-spacing: 0.5px;
    color: var(--gold);
  }
  .promo-tagline span { display: block; }
  .promo-tagline .line-2 { padding-left: 14px; }
  .promo-tagline .line-3 { padding-left: 28px; }
  .promo-contact {
    position: absolute;
    left: 64px;
    bottom: 28px;
    font-family: "Arimo", sans-serif;
    font-size: 18px;
    line-height: 1.25;
    color: var(--gold);
  }
  .promo-contact .website { padding-left: 10px; }

  /* Front side: studio name */
  .brand {
    position: absolute;
    inset: 0;
    display: flex;
    align-items: center;
    justify-content: center;
    gap: 12px;
  }
  .brand-dot {
    width: 14px;
    height: 14px;
    border-radius: 50%;
    background: var(--gold);
  }
  .brand-name {
    font-family: "Arimo", sans-serif;
    font-weight: 700;
    font-size: 26px;
    letter-spacing: 2px;
    text-transform: uppercase;
    color: var(--gold);
  }
</style>
</head>
<body>
  <main class="stage">
    <section class="card card-back">
      <div class="promo-artwork" role="img" aria-label="Large blind-embossed cat head silhouette, black on black"></div>
      <h1 class="promo-tagline">
        <span class="line-1">Your path to</span>
        <span class="line-2">success</span>
        <span class="line-3">starts here</span>
      </h1>
      <p class="promo-contact">
        <span class="phone">0742163958</span><br>
        <span class="website">www.velmastrand.ro</span>
      </p>
    </section>

    <section class="card card-front">
      <div class="brand">
        <span class="brand-dot"></span>
        <span class="brand-name">Velma Strand Studio</span>
      </div>
    </section>
  </main>
</body>
</html>
```